THE HOMESTEAD PIVOT
Project: THE HOMESTEAD PIVOT
THE HOMESTEAD PIVOT  - Real Estate
Creative Brief
"THE HOMESTEAD PIVOT" is a new and upcoming real estate company. Very modern,Very Professional. With the help of Mark Craft Studio we now have company logo and stationary. We now need real estate yard signs...... We need a designer to take the company logo and other information and design a very professional, unique, modern yard sign that grabs your attention as you travel past. See attached picture for a normal yard sign. Note: The yard sign has two parts. Part one is an insert for individual name and phone number. Part two is the body of the sign with the words For Sale, logo and phone number. KEEP IN MIND - The sign frame will be forty two inches tall by twenty four inches wide. It will be taller than the normal yard sign. USE THE FOLLOWING INFORMATION ON SIGN: > CALVIN MORRISEY > 415-722-6143 > FOR SALE > LOGO - Ai file attached. THANKS FOR THE HELP.... GOOD LUCK.....
Real Estate
GENERAL PUBLIC IS AUDIENCE. STYLISH, PROFESSIONAL GRABS YOUR ATTENTION. MODERN
> USE COLOR SCHEME = IN LOGO AND STATIONARY. Ai file attached. > USE THIS INFORMATION: CALVIN MORRISEY 415-722-6143, FOR SALE, LOGO - Ai file attached.

```html
<!DOCTYPE html>
<html lang="en">
<head>
<meta charset="utf-8">
<title>The Homestead Pivot – Yard Sign</title>
<link rel="stylesheet" href="https://fonts.googleapis.com/css2?family=Anton&family=Roboto+Condensed:wght@700&display=swap">
<style>
  :root {
    --page: #eef0f2;
    --frame: #121212;
    --panel-black: #161616;
    --sale-orange: #f2641c;
    --gold: #c9a24a;
    --cream-top: #f4ecd6;
    --cream-bottom: #d9c594;
    --brand-brown: #5a3b1c;
    --white: #ffffff;
    --rider-yellow: #f5d56a;
  }
  * { box-sizing: border-box; margin: 0; padding: 0; }
  html, body { width: 1200px; height: 1014px; overflow: hidden; }
  body { background: var(--page); position: relative; font-family: "Roboto Condensed", Arial, sans-serif; }

  .sign { position: absolute; left: 380px; top: 30px; width: 440px; height: 970px; }

  .post { position: absolute; top: 0; width: 22px; height: 970px; background: var(--frame); }
  .post--left { left: 0; }
  .post--right { right: 0; }

  .rider {
    position: absolute; left: 0; top: 0; width: 440px; height: 150px;
    background: var(--panel-black); border: 6px solid var(--frame);
    display: flex; align-items: center; padding: 0 34px; gap: 22px;
  }
  .rider__icon { width: 46px; height: 70px; flex: none; }
  .rider__text { display: flex; flex-direction: column; gap: 6px; }
  .rider__name { color: var(--white); font-size: 40px; line-height: 1; }
  .rider__phone { color: var(--rider-yellow); font-size: 40px; line-height: 1; }

  .board {
    position: absolute; left: 0; top: 172px; width: 440px; height: 700px;
    border: 8px solid var(--frame); background: var(--panel-black);
    display: flex; flex-direction: column;
  }
  .board__headline {
    height: 150px; display: flex; align-items: center; justify-content: center;
    font-family: "Anton", Impact, sans-serif; font-size: 84px; letter-spacing: 1px;
    color: var(--sale-orange);
  }
  .board__rule { height: 8px; background: var(--gold); }
  .board__brand {
    flex: 1; background: linear-gradient(180deg, var(--cream-top), var(--cream-bottom));
    display: flex; flex-direction: column; align-items: center; justify-content: center; gap: 18px;
  }
  .brand__mark { width: 40px; height: 40px; border-radius: 50%; background: var(--brand-brown); }
  .brand__name {
    font-family: "Anton", Impact, sans-serif; font-size: 44px; line-height: 1.1;
    color: var(--brand-brown); text-align: center; letter-spacing: 1px;
  }
  .board__phone {
    height: 130px; display: flex; align-items: center; justify-content: center;
    color: var(--white); font-size: 62px;
  }
</style>
</head>
<body>
  <div class="sign">
    <div class="post post--left"></div>
    <div class="post post--right"></div>

    <div class="rider">
      <svg class="rider__icon" viewBox="0 0 46 70" aria-hidden="true">
        <rect x="4" y="2" width="38" height="66" rx="7" fill="#ffffff"/>
        <rect x="9" y="10" width="28" height="40" fill="#161616"/>
        <circle cx="23" cy="59" r="4" fill="#161616"/>
      </svg>
      <div class="rider__text">
        <span class="rider__name">Calvin Morrisey</span>
        <span class="rider__phone">415-722-6143</span>
      </div>
    </div>

    <div class="board">
      <div class="board__headline">FOR SALE</div>
      <div class="board__rule"></div>
      <div class="board__brand">
        <div class="brand__mark"></div>
        <div class="brand__name">THE HOMESTEAD<br>PIVOT</div>
      </div>
      <div class="board__rule"></div>
      <div class="board__phone">415-722-6143</div>
    </div>
  </div>
</body>
</html>
```